Ayurveda & Wellness Website Redesign.

I need my website www.palvoreta.com re-skinned. It is a wordpress site with Velo Framer.
I need a clearer funnel for new clients on the home page.
The funnel should provide questions for the potential client to answer. I can provide these, but I need a better funnel mechanism I think,
Possibly a video on the home page. Or an area of a video that I can change out.
So a better landing page is KEY!
The funnel should reroute to a video page and I should get informed when new clients enroll in the funnel.
Maybe I need a management system for this, but I need a recommendation.
Now I am using forms manager.
I need to be able to make changes using wordpress and/or Velo Framer.
The website should have a clean and spiritual feeling.
I can provide many more pictures and higher resolution.
I like the feeling of this website: http://brightfernherbals.com
Also this website: http://lotuscalmhaven.com/sessionswithkoriel/
Target Market(s)
Women ages 25-65. People interested in health, yoga, spirituality.
Industry/Entity Type
Health And Wellness
Coding
Coded - Design and coding required
Requirements
Must have
- A clear sales funnel/enrollment mechanism on the home page. Could have a ebook download (I will provide) when they enroll.
Nice to have
- Currently using Slotra for clients to enroll in appointments. I would like to keep this.

```html
<!DOCTYPE html>
<html lang="en">
<head>
<meta charset="utf-8">
<title>Lotus Ease – Ayurveda & Wellness</title>
<link href="https://fonts.googleapis.com/css2?family=Open+Sans:wght@400;600;700&family=Playfair+Display:wght@700&display=swap" rel="stylesheet">
<style>
:root{
  --plum:#5b2a6f;
  --plum-deep:#3a1450;
  --violet:#8e55b8;
  --ink:#333;
  --muted:#666;
  --line:#e3e3e3;
  --sand:#f6efc0;
  --sage:#e7edc6;
  --sage-deep:#cfd9a2;
  --white:#fff;
}
*{box-sizing:border-box;margin:0;padding:0}
html,body{width:1200px;height:3436px;overflow:hidden}
body{font-family:"Open Sans",Arial,sans-serif;color:var(--ink);background:var(--white);position:relative}
.abs{position:absolute}

/* top bar */
.topbar{top:0;left:0;width:1200px;height:32px;background:var(--plum-deep);color:#ddd;font-size:11px;display:flex;align-items:center;gap:24px;padding-left:72px}
.topbar span{display:flex;align-items:center;gap:6px}

/* header */
.header{top:32px;left:0;width:1200px;height:98px;background:var(--white);border-bottom:1px solid var(--line)}
.brand{left:72px;top:30px;display:flex;align-items:center;gap:10px;font-size:28px;font-weight:600;color:var(--plum)}
.brand i{width:14px;height:14px;border-radius:50%;background:var(--violet);display:block}
.nav{right:60px;top:40px;display:flex;gap:22px;font-size:12px;font-weight:600;text-transform:uppercase;letter-spacing:.5px;color:#555}
.nav .on{color:var(--violet);background:#f1e8f7;padding:4px 8px;margin-top:-4px}

/* hero */
.hero{top:130px;left:0;width:1200px;height:600px;background:radial-gradient(circle at 76% 45%,#f6e9ff 0,#c79ae6 14%,#8a47b9 38%,#5a1f88 65%,#3a0f5e 100%)}
.hero-copy{left:184px;top:180px;color:var(--white)}
.hero-copy h1{font-size:28px;font-weight:700;letter-spacing:2px;margin-bottom:30px}
.hero-copy p{font-size:18px;font-weight:600;margin-bottom:18px}
.btn-ghost{display:inline-block;margin-top:22px;border:2px solid var(--white);padding:10px 16px;font-size:14px;color:var(--white)}

/* ayurveda intro */
.intro-img{left:208px;top:820px;width:200px;height:200px;border-radius:6px;background:linear-gradient(135deg,#b98ad0,#6d3b8b 55%,#c9b7a0)}
.intro-copy{left:450px;top:840px;width:560px}
.intro-copy h2{font-size:22px;font-weight:600;color:var(--ink);margin-bottom:16px}
.intro-copy p{font-size:13px;line-height:1.6;color:var(--muted)}
.learn{margin-top:24px;display:flex;align-items:center;gap:10px;font-size:12px;font-weight:700}
.learn i{width:22px;height:22px;border-radius:50%;background:var(--plum);display:block}

/* intake form */
.intake{top:1110px;left:0;width:1200px;height:560px;background:linear-gradient(180deg,#f7b64a 0,#f08a2a 45%,#d9551e 78%,#4a2412 100%)}
.intake-box{left:208px;top:1188px;width:712px;height:380px;background:rgba(250,240,190,.86);padding:18px 22px;font-size:11px;color:#444}
.intake-box b{display:block;font-size:11px;margin-bottom:10px}
.row{display:flex;align-items:center;gap:10px;margin-bottom:12px}
.row label{width:70px}
.field{background:var(--white);border:1px solid #ccc;height:20px}
.hr{border-top:1px solid #bbb;margin:16px 0}
.btn-plum{display:inline-block;background:var(--plum);color:var(--white);font-size:11px;padding:5px 12px}

/* testimonials */
.testi{top:1690px;left:0;width:1200px;text-align:center}
.testi h2{font-family:"Playfair Display",Georgia,serif;color:var(--plum);font-size:28px;margin-top:30px}
.testi p{width:960px;margin:90px auto 0;font-size:14px;line-height:1.65;color:#444}
.testi .by{margin-top:28px;font-weight:700}

/* contact */
.contact{top:2192px;left:0;width:1200px;height:596px;background:linear-gradient(90deg,#ffffff 0,#f3f3ee 35%,#e8ecd6 70%,#dfe6c4 100%)}
.figure{left:130px;top:2250px;width:200px;height:460px;background:linear-gradient(180deg,#efe9e4,#d9d2cc);border-radius:4px}
.contact-box{left:488px;top:2272px;width:532px;height:416px;background:rgba(234,239,196,.9);padding:20px 22px;font-size:11px;color:#444}
.contact-box .row label{width:100px}
.sub{font-size:9px;color:#777}

/* chakras */
.chakras{top:2912px;left:0;width:1200px;display:flex;justify-content:center;gap:22px}
.chakras i{width:72px;height:72px;border-radius:50%;display:block;border:6px solid rgba(255,255,255,.6);box-shadow:0 0 0 3px currentColor;background:currentColor}

/* footer */
.footer{top:3088px;left:0;width:1200px;height:312px;background:var(--sage);padding:36px 72px;display:flex;gap:60px;font-size:12px;color:#555}
.footer h4{font-size:13px;color:var(--ink);margin-bottom:16px}
.footer p{line-height:1.6}
.footer ul{list-style:none;line-height:1.9}
.footer li::before{content:"› ";color:var(--plum)}
.copy{top:3400px;left:0;width:1200px;height:36px;background:var(--sage-deep);font-size:11px;color:#666;text-align:center;line-height:36px}
</style>
</head>
<body>

<div class="abs topbar">
  <span><svg width="10" height="10" viewBox="0 0 10 10"><path d="M2 1l2 2-1 1.5c.6 1.2 1.3 1.9 2.5 2.5L7 6l2 2-1.5 1.5C4 9 1 6 .5 2.5z" fill="#ddd"/></svg>+1 555 014 2287</span>
  <span><svg width="12" height="9" viewBox="0 0 12 9"><rect x=".5" y=".5" width="11" height="8" fill="none" stroke="#ddd"/><path d="M.5.5l5.5 4 5.5-4" fill="none" stroke="#ddd"/></svg>hello@lotusease.com</span>
</div>

<header class="abs header">
  <div class="abs brand"><i></i>Lotus Ease</div>
  <nav class="abs nav">
    <span class="on">Home</span><span>Consults</span><span>Ayurveda</span><span>About Marisol</span><span>Workshops</span><span>Follow the Blog</span><span>Contact Us</span>
  </nav>
</header>

<section class="abs hero" role="img" aria-label="Glowing white lotus flower on still water under a purple sky with sparkles"></section>
<div class="abs hero-copy">
  <h1>LOTUS EASE WITH AYURVEDA</h1>
  <p>Find your center with Ayurveda</p>
  <p>An experience of personal transformation</p>
  <span class="btn-ghost">Get Started Today !</span>
</div>

<div class="abs intro-img" role="img" aria-label="Purple flowers beside a small sign reading Ayurveda"></div>
<div class="abs intro-copy">
  <h2>Ayurveda</h2>
  <p>Ayurveda is the “science of life.” It is a system of wellness that works with nature to correct imbalances and to maintain balance in the body, mind and spirit.</p>
  <div class="learn"><i></i>Learn More</div>
</div>

<section class="abs intake" role="img" aria-label="Silhouette of a woman meditating in front of an orange sunset"></section>
<form class="abs intake-box">
  <b>What is your Birth date, time and place (If you do not know the time please give the date and place this will allow Dr. Venn to look at your Vedic astrological chart.</b>
  <div class="row"><label>Birth Date</label><span class="field" style="width:160px"></span></div>
  <div class="row"><label>Birth Time</label><span class="field" style="width:26px"></span><span class="field" style="width:26px"></span><span class="field" style="width:26px"></span></div>
  <div class="row"><label>Birth Place</label><span class="field" style="width:300px"></span></div>
  <div class="hr"></div>
  <b>On a scale of 1-10 with 1 being like a tiger and 10 being a sleeping dog</b>
  <div class="row"><label style="width:200px">How physically active are you?</label><span class="field" style="width:200px;font-size:9px;padding:3px">Select value</span></div>
  <div class="hr"></div>
  <span class="btn-plum">Submit</span> <span style="margin-left:8px">Reset</span>
</form>

<section class="abs testi">
  <h2>Testimonials</h2>
  <p>After Marisol’s attentive questions, feeling of my pulses, and intuitive observation, she prescribed for me a blend of herbs and suggestions for my diet that allow me to sleep through the night without my previous fiery constitution waking me up. Her blend of humor, humility and inquiry are a powerful combination – her very manner is one that promotes healthfulness. I have had private consultations with Marisol, and have attended workshops on Ayurveda; I always learn things that are useful and applicable to my daily life, and am continually disarmed by her warmth and kindness.</p>
  <div class="by">M.S</div>
</section>

<section class="abs contact" role="img" aria-label="Soft pale flowers on a light green background"></section>
<div class="abs figure" role="img" aria-label="Woman in black yoga clothes kneeling in meditation"></div>
<form class="abs contact-box">
  <div class="row"><label>Name *</label><span class="field" style="width:110px"></span><span class="field" style="width:110px"></span></div>
  <div class="row sub"><label></label><span style="width:110px">First</span><span>Last</span></div>
  <div class="row"><label>Phone *</label><span class="field" style="width:36px"></span><span class="field" style="width:36px"></span><span class="field" style="width:50px"></span></div>
  <div class="row sub"><label></label><span>### ### ####</span></div>
  <div class="row"><label>E-mail</label><span class="field" style="width:240px"></span></div>
  <div class="row" style="align-items:flex-start"><label>Message</label><span class="field" style="width:240px;height:80px"></span></div>
  <div class="row"><label>Word Verification</label><span class="field" style="width:80px"></span><span class="field" style="width:70px;height:26px;background:#e9e9e9"></span></div>
  <div class="row" style="margin-top:20px"><span class="btn-plum">Submit</span><span class="btn-plum">Reset</span></div>
</form>

<div class="abs chakras" aria-label="Seven chakra colours">
  <i style="color:#d8262b"></i><i style="color:#f08a1c"></i><i style="color:#f3c91c"></i><i style="color:#5cad3b"></i><i style="color:#2d9fd8"></i><i style="color:#3a4fa8"></i><i style="color:#7b3f9e"></i>
</div>

<footer class="abs footer">
  <div style="width:380px">
    <h4>About Marisol</h4>
    <p>I am passionate about energy renewal and helping people resolve their health imbalances. Marisol has been studying and teaching about Ayurveda for many years and is a certified Clinical Ayurveda practitioner, spiritual counselor and yoga teacher who guides others on their own path home.</p>
  </div>
  <div style="width:300px">
    <h4>Quick Links</h4>
    <ul><li>About Marisol</li><li>Consults</li><li>Ayurveda</li><li>Workshops</li></ul>
  </div>
  <div>
    <h4>Contact Us</h4>
    <p>Tel : +1 555 014 2287</p>
    <p style="margin-top:8px">Email : hello@lotusease.com</p>
  </div>
</footer>
<div class="abs copy">© 2017 Lotus Ease. All Rights Reserved.</div>

</body>
</html>
```